Serlivo Business Cards

We need new Business Cards for our startup. It just launched.It is working in the high-end it-market. Specifically in the cloud area. We are a hybrid cloud company. The company logo is attached. We are a Swiss based company. Information visible on the card is: 1. Logo 2. Company Name: Serlivo AG 3. Subtitle: Hybrid Clouds. 3. Name: Tobias Ferrand 4. Adress: Lindenhofweg 14a, 8472 Halvingen, Switzerland 5. Email: tobias@serlivo-mail.ch. 6. Mobile: +41 79 386 42 15. It should be a grey/white design. Similar to the attached logo. It should have class, high-quality but not too much color and no gold used.
Updates

I forgot to add my Position. Please use Founder / CEO. thanks tobias

Industry/Entity Type

Business

```html
<!DOCTYPE html>
<html lang="en">
<head>
<meta charset="UTF-8">
<title>Serlivo Business Card</title>
<link rel="stylesheet" href="https://fonts.googleapis.com/css2?family=Source+Sans+3:wght@300;400&display=swap">
<style>
  :root {
    --page-bg: #3b3b3b;
    --card-bg: #ffffff;
    --band: #6d6d6d;
    --rule: #8a8a8a;
    --ink: #5c5c5c;
    --ink-soft: #666666;
    --mark: #bdbdbd;
    --cloud-light: #f2f2f2;
    --cloud-dark: #a9a9a9;
    --on-band: #ffffff;
  }
  * { margin: 0; padding: 0; box-sizing: border-box; }
  html, body {
    width: 1200px; height: 750px; overflow: hidden;
    background: var(--page-bg);
    font-family: "Source Sans 3", "Myriad Pro", Arial, sans-serif;
    font-weight: 400;
  }
  .business-card {
    position: absolute; left: 100px; top: 88px;
    width: 1000px; height: 575px;
    background: var(--card-bg);
    overflow: hidden;
    box-shadow: 0 6px 18px rgba(0,0,0,0.45);
  }
  .brand-mark {
    position: absolute; left: 150px; top: 70px;
    width: 92px; height: 92px; border-radius: 50%;
    background: var(--mark);
  }
  .brand-name {
    position: absolute; left: 408px; top: 88px;
    font-size: 62px; font-weight: 300; letter-spacing: 14px; line-height: 1;
    color: var(--ink);
  }
  .name-band {
    position: absolute; left: 0; top: 221px;
    width: 100%; height: 81px;
    background: var(--band);
    display: flex; align-items: center;
    padding-left: 49px; color: var(--on-band);
  }
  .person-name { font-size: 35px; }
  .person-role {
    font-size: 29px; margin-left: 12px; padding-left: 12px;
    border-left: 2px solid var(--on-band); line-height: 1.1;
  }
  .band-rule {
    position: absolute; left: 0; top: 306px; width: 100%;
    height: 2px; background: var(--rule);
  }
  .company {
    position: absolute; left: 49px; top: 318px;
    color: var(--ink-soft);
  }
  .company-name { font-size: 31px; line-height: 42px; }
  .company-tagline { font-size: 29px; line-height: 40px; }
  .contact-list {
    position: absolute; right: 48px; top: 318px;
    list-style: none; color: var(--ink-soft);
    z-index: 1;
  }
  .contact-item {
    display: flex; justify-content: flex-end; align-items: center;
    font-size: 29px; height: 42px;
  }
  .contact-icon { width: 22px; height: 22px; margin-left: 22px; flex: none; }
  .contact-item.no-icon { padding-right: 44px; }
  .cloud-border {
    position: absolute; left: 0; bottom: 0; width: 100%; height: 88px;
    background: linear-gradient(180deg, var(--cloud-light) 0%, var(--cloud-dark) 100%);
  }
</style>
</head>
<body>
  <article class="business-card">
    <div class="brand-mark"></div>
    <div class="brand-name">SERLIVO</div>

    <div class="name-band">
      <span class="person-name">Tobias Ferrand</span>
      <span class="person-role">Founder / CEO</span>
    </div>
    <div class="band-rule"></div>

    <div class="company">
      <div class="company-name">Serlivo AG 3</div>
      <div class="company-tagline">Hybrid Clouds</div>
    </div>

    <ul class="contact-list">
      <li class="contact-item">+41 79 386 42 15
        <svg class="contact-icon" viewBox="0 0 22 22"><rect x="6" y="2" width="10" height="18" rx="1.5" fill="none" stroke="#666" stroke-width="1.6"/></svg>
      </li>
      <li class="contact-item">tobias@serlivo-mail.ch
        <svg class="contact-icon" viewBox="0 0 22 22"><rect x="3" y="6" width="16" height="11" fill="#666"/><path d="M3 6 L11 12 L19 6" fill="none" stroke="#fff" stroke-width="1.4"/></svg>
      </li>
      <li class="contact-item">Lindenhofweg 14a
        <svg class="contact-icon" viewBox="0 0 22 22"><path d="M11 2 C6.5 2 4.5 5.5 4.5 8.5 C4.5 13 11 20 11 20 C11 20 17.5 13 17.5 8.5 C17.5 5.5 15.5 2 11 2 Z" fill="#666"/><circle cx="11" cy="8.5" r="2.5" fill="#fff"/></svg>
      </li>
      <li class="contact-item no-icon">8472 Halvingen, Switzerland</li>
    </ul>

    <div class="cloud-border" role="img" aria-label="Decorative border of soft grey clouds along the bottom edge"></div>
  </article>
</body>
</html>
```